Harbor Vantage Web Design Project

We need a website design for a start up company called "Harbor Vantage". We provide business consultancy services as well as technology-related services (IT). The design should communicate simplicity and elegance. The domain name of the site will be harborvantage-example.com. The logo of the company is https://files.example-share.net/u/7418205/4630_2116587_67315_image.jpg

Target Market(s)

SMB, Corporates, Semi-governments, Governments.

Industry/Entity Type

Business

Requirements
Must have
• - The background of the pages should be white or soft grey, but we are open for suggestions.
- The pages should have nice menu animations.
- The pages should be "portal-style", with multiple placeholders for different sections and multiple tabs.
Nice to have
• The page should auto-fit the screen and scroll vertically as much as needed.
Should not have
• - Flash Animations.
- Generic Photos.

```html
<!DOCTYPE html>
<html lang="en">
<head>
<meta charset="utf-8">
<title>Harbor Vantage</title>
<link href="https://fonts.googleapis.com/css2?family=Ubuntu:ital,wght@0,300;0,400;0,500;0,700;1,400;1,500&display=swap" rel="stylesheet">
<style>
  :root{
    --topbar:#2a2a2a;
    --topbar-pill:#3a3a3a;
    --topbar-text:#e6e6e6;
    --nav-top:#f4f4f4;
    --nav-bottom:#dcdcdc;
    --nav-text:#6b6b6b;
    --nav-active-top:#6f9bc7;
    --nav-active-bottom:#3e6e9f;
    --hero-top:#d7eef9;
    --hero-bottom:#f3f9fc;
    --title:#4a5a5c;
    --body:#4e4e4e;
    --muted:#9a9a9a;
    --btn-top:#c9ecfb;
    --btn-bottom:#85cdee;
    --btn-border:#6bb7dc;
    --quote-bg:#f8f8f8;
    --rule:#e2e2e2;
    --quote-mark:#bdbdbd;
    --brand:#2c4f86;
  }
  *{box-sizing:border-box;margin:0;padding:0}
  html,body{width:1200px;height:1200px;overflow:hidden;background:#fff}
  body{font-family:"Ubuntu",sans-serif;color:var(--body);position:relative}

  .topbar{position:absolute;left:0;top:0;width:1200px;height:38px;background:var(--topbar)}
  .utility{position:absolute;left:520px;top:8px;display:flex;gap:6px}
  .utility a{display:flex;align-items:center;gap:5px;height:22px;padding:0 9px;border-radius:11px;background:var(--topbar-pill);color:var(--topbar-text);font-size:10px;text-decoration:none;box-shadow:inset 0 1px 0 rgba(255,255,255,.08)}
  .utility svg{width:10px;height:10px;fill:none;stroke:var(--topbar-text);stroke-width:1.4}
  .social{position:absolute;left:900px;top:8px;display:flex;gap:5px}
  .social span{width:22px;height:22px;border-radius:50%;background:var(--topbar-pill)}

  .navbar{position:absolute;left:0;top:38px;width:1200px;height:56px;background:linear-gradient(var(--nav-top),var(--nav-bottom));border-bottom:1px solid #cfcfcf}
  .brand{position:absolute;left:242px;top:16px;display:flex;align-items:center;gap:8px}
  .brand i{width:20px;height:20px;border-radius:50%;background:var(--brand)}
  .brand b{font-weight:500;font-size:22px;color:var(--brand)}
  .menu{position:absolute;left:567px;top:0;height:56px;display:flex}
  .menu a{display:flex;align-items:center;padding:0 9px;font-size:11px;color:var(--nav-text);text-decoration:none;border-right:1px solid #d0d0d0;transition:background .3s}
  .menu a:hover{background:rgba(255,255,255,.6)}
  .menu a.current{background:linear-gradient(var(--nav-active-top),var(--nav-active-bottom));color:#fff;font-weight:700;padding:0 12px}

  .hero{position:absolute;left:0;top:94px;width:1200px;height:552px;background:linear-gradient(170deg,var(--hero-top),var(--hero-bottom) 70%)}
  .hero h1{position:absolute;left:220px;top:184px;font-weight:300;font-size:57px;color:var(--title);letter-spacing:.5px}
  .hero h2{position:absolute;left:224px;top:246px;font-weight:400;font-size:16px;color:var(--title)}
  .hero p{position:absolute;left:224px;top:273px;width:280px;font-size:10.5px;line-height:17.6px;color:var(--body)}
  .btn-tour{position:absolute;left:224px;top:334px;width:232px;height:36px;border-radius:3px;background:linear-gradient(var(--btn-top),var(--btn-bottom));border:1px solid var(--btn-border);font-size:16px;color:#2e4a5a;display:flex;align-items:center;justify-content:center;box-shadow:0 2px 3px rgba(0,0,0,.2)}
  .hero-art{position:absolute;left:536px;top:10px;width:648px;height:530px;border-radius:50%;background:radial-gradient(ellipse at 45% 60%,#bfe3f4 0,#e8d7c4 30%,#cfe8c0 45%,rgba(240,248,252,0) 70%)}
  .slider-dots{position:absolute;left:576px;top:528px;display:flex;gap:9px}
  .slider-dots span{width:10px;height:10px;border-radius:50%;background:#c6c6c6;border:1px solid #b4b4b4}

  .testimonial{position:absolute;left:0;top:646px;width:1200px;height:126px;background:var(--quote-bg);border-top:1px solid var(--rule);border-bottom:1px solid var(--rule)}
  .mark{position:absolute;font-family:Georgia,serif;font-weight:700;color:var(--quote-mark);font-size:150px;line-height:1}
  .mark.open{left:134px;top:-18px}
  .mark.close{left:984px;top:16px}
  .testimonial h3{position:absolute;left:223px;top:24px;font-weight:300;font-size:16px;color:var(--title)}
  .testimonial p{position:absolute;left:223px;top:44px;width:748px;font-size:10.3px;line-height:16px}
  .author{position:absolute;right:236px;top:84px;text-align:right;font-style:italic;color:#777}
  .author strong{display:block;font-weight:500;font-size:11.5px}
  .author span{font-size:10px}

  .features{position:absolute;left:224px;top:824px;display:flex;gap:15px}
  .feature{width:240px;text-align:center}
  .feature svg{display:block;width:240px;height:146px}
  .feature h4{margin-top:16px;font-weight:300;font-size:24px;color:var(--title);line-height:28px}
  .feature .tag{font-size:13.5px;font-weight:300;color:var(--muted);margin-top:2px;padding-bottom:10px;border-bottom:1px solid #ccc}
  .feature p{font-size:10.3px;line-height:16px;margin-top:9px;padding:0 4px}
  .btn-start{display:inline-flex;margin-top:12px;width:132px;height:25px;align-items:center;justify-content:center;border-radius:2px;background:linear-gradient(var(--btn-top),var(--btn-bottom));border:1px solid var(--btn-border);font-size:11px;color:#34505e;box-shadow:0 2px 2px rgba(0,0,0,.18)}
  .footer-rule{position:absolute;left:0;top:1192px;width:1200px;height:1px;background:var(--rule)}
</style>
</head>
<body>
  <header class="topbar">
    <nav class="utility">
      <a href="#"><svg viewBox="0 0 10 10"><circle cx="5" cy="3" r="2"/><path d="M1 10c0-3 8-3 8 0"/></svg>Client Login</a>
      <a href="#"><svg viewBox="0 0 10 10"><circle cx="5" cy="5" r="4"/><circle cx="5" cy="5" r="1.8"/></svg>Support</a>
      <a href="#"><svg viewBox="0 0 10 10"><rect x=".7" y="2" width="8.6" height="6"/><path d="M1 2l4 3 4-3"/></svg>Email</a>
      <a href="#"><svg viewBox="0 0 10 10"><path d="M1 1h4l4 4-4 4-4-4z"/></svg>Sales</a>
      <a href="#"><svg viewBox="0 0 10 10"><rect x="1" y="1" width="8" height="6"/><path d="M3 7v2l2-2"/></svg>Live Chat</a>
    </nav>
    <div class="social"><span></span><span></span><span></span></div>
  </header>

  <div class="navbar">
    <div class="brand"><i></i><b>Harbor Vantage</b></div>
    <nav class="menu">
      <a href="#" class="current">Home</a>
      <a href="#">About</a>
      <a href="#">Comapny</a>
      <a href="#">Services</a>
      <a href="#">Solutions</a>
      <a href="#">Clients</a>
      <a href="#">Contact Us</a>
    </nav>
  </div>

  <section class="hero">
    <div class="hero-art" role="img" aria-label="Illustration of a cloud with a user profile card, linked by colourful swirling lines to floating web service icons, stars and hearts"></div>
    <h1>Cloud solutions</h1>
    <h2>your own personal cloud</h2>
    <p>This is Photoshop's version of Lorem Ipsum. Proin gravida nibh vel velit auctor aliquet. Aenean sollicitudin, lorem quis bibendum auctor, nisi elit consequat</p>
    <a class="btn-tour">Take a quick tour</a>
    <div class="slider-dots"><span></span><span></span><span></span></div>
  </section>

  <section class="testimonial">
    <div class="mark open">“</div>
    <h3>Networking is now much more Fun !!</h3>
    <p>Lorem Ipsum. Proin gravida nibh vel velit auctor aliquet. Aenean sollicitudin, lorem quis bibendum auctor, nisi elit consequat ipsum, nec sagittis sem nibh id elit. Duis sed odio sit amet nibh vulputate cursus a sit amet mauris. Morbi accumsan ipsum velit. Nam nec tellus a odio tincidunt auctor a ornare odio. Sed non mauris vitae erat consequat auctor eu in elit.</p>
    <div class="author"><strong>Dara Moreno</strong><span>Founder and CEO, Northfield Media Group</span></div>
    <div class="mark close">”</div>
  </section>

  <section class="features">
    <article class="feature">
      <svg viewBox="0 0 240 146" role="img" aria-label="Cloud-shaped photo of a support agent wearing a headset microphone">
        <defs><linearGradient id="g1" gradientUnits="userSpaceOnUse" x1="0" y1="0" x2="240" y2="146"><stop offset="0" stop-color="#f3e1d3"/><stop offset=".5" stop-color="#e4a98a"/><stop offset="1" stop-color="#f2ede8"/></linearGradient></defs>
        <g fill="url(#g1)"><circle cx="138" cy="72" r="72"/><circle cx="42" cy="106" r="40"/><circle cx="205" cy="110" r="35"/><rect x="40" y="100" width="165" height="46"/></g>
      </svg>
      <h4>Personal Cloud</h4>
      <div class="tag">Lorem velit auctor aliqet aeneam</div>
      <p>Lorem velit auctor aliquet. Aenean sollicitudin, lorem quis bibendum auctor, nisi elit consequat ipsum, nec sagittis sem nibh id elit.</p>
      <a class="btn-start">Get Started</a>
    </article>
    <article class="feature">
      <svg viewBox="0 0 240 146" role="img" aria-label="Cloud-shaped photo of two business people shaking hands">
        <defs><linearGradient id="g2" gradientUnits="userSpaceOnUse" x1="0" y1="0" x2="240" y2="146"><stop offset="0" stop-color="#f1f1f1"/><stop offset=".5" stop-color="#dcb59a"/><stop offset="1" stop-color="#2a2a2a"/></linearGradient></defs>
        <g fill="url(#g2)"><circle cx="138" cy="72" r="72"/><circle cx="42" cy="106" r="40"/><circle cx="205" cy="110" r="35"/><rect x="40" y="100" width="165" height="46"/></g>
      </svg>
      <h4>Better Service</h4>
      <div class="tag">Lorem velit auctor aliqet aeneam</div>
      <p>Lorem velit auctor aliquet. Aenean sollicitudin, lorem quis bibendum auctor, nisi elit consequat ipsum, nec sagittis sem nibh id elit.</p>
      <a class="btn-start">Get Started</a>
    </article>
    <article class="feature">
      <svg viewBox="0 0 240 146" role="img" aria-label="Cloud-shaped image of glowing blue computer monitors and data streams">
        <defs><linearGradient id="g3" gradientUnits="userSpaceOnUse" x1="0" y1="0" x2="240" y2="146"><stop offset="0" stop-color="#0e4f7a"/><stop offset=".5" stop-color="#7fd0ee"/><stop offset="1" stop-color="#1a6c9c"/></linearGradient></defs>
        <g fill="url(#g3)"><circle cx="138" cy="72" r="72"/><circle cx="42" cy="106" r="40"/><circle cx="205" cy="110" r="35"/><rect x="40" y="100" width="165" height="46"/></g>
      </svg>
      <h4>New Technology</h4>
      <div class="tag">Lorem velit auctor aliqet aeneam</div>
      <p>Lorem velit auctor aliquet. Aenean sollicitudin, lorem quis bibendum auctor, nisi elit consequat ipsum, nec sagittis sem nibh id elit.</p>
      <a class="btn-start">Get Started</a>
    </article>
  </section>

  <div class="footer-rule"></div>
</body>
</html>
```